Business Card for supplement company

Company Name: Pinevale Nutrition
We require quite a simple yet stand out business card for our supplement company.
We are selling high end bodybuilding supplements direct to the public through online sales and Facebook marketing.
There will be slightly varying versions of the card and the winning design will be required to make these slight adjustments.
We will also require the file to be provided in and editable version as we will have a discount code on there that will be changed for different people.
Employee Cards:
Logo on the front of the card (see attached EPS file)
Please also add slogan in text "When Failure is Not and Option" as close as possible to what is seen in this link www.pinevalenutrition.com.au
Suggestions: Card in black, possibly use a similar background to website theme (honeycomb, carbon look)
Information to be included on the back (please place and order accordingly)
:Clive Marrowby (Director)
Email: clive@pinevalenutrition.com.au
Phone: 02 5918 2273
Website: www.pinevalenutrition.com.au
Athlete Cards:
Front:
Same as above
Back:
Discount Code: xxx123 (to be editable)
Facebook: www.facebook.com/PinevaleNutrition
Design ideas: please look at our website and facebook signup page for design ideas.

```html
<!DOCTYPE html>
<html lang="en">
<head>
<meta charset="utf-8">
<title>Pinevale Nutrition – Business Card</title>
<link href="https://fonts.googleapis.com/css2?family=Lato:wght@400;700;900&display=swap" rel="stylesheet">
<style>
  :root {
    --backdrop: #d9d6d2;
    --card: #2a2a2b;
    --card-edge: #1f1f20;
    --texture: #333335;
    --green: #4fae3a;
    --green-deep: #2f7d2a;
    --gold: #e6c31e;
    --white: #f2f2f2;
    --silver: #d8d8d8;
  }
  * { margin: 0; padding: 0; box-sizing: border-box; }
  html, body { width: 1200px; height: 900px; overflow: hidden; }
  body {
    background: var(--backdrop);
    font-family: "Lato", Arial, sans-serif;
    position: relative;
  }
  .card {
    position: absolute;
    left: 353px;
    width: 489px;
    height: 280px;
    background: var(--card);
    border-radius: 2px;
    box-shadow: 0 2px 6px rgba(0,0,0,0.35);
    overflow: hidden;
  }
  .card--front { top: 153px; }
  .card--back { top: 463px; }

  .texture {
    position: absolute;
    inset: 0;
  }
  .card--front .texture {
    background: linear-gradient(180deg, var(--texture) 0%, rgba(51,51,53,0.4) 45%, var(--texture) 100%);
  }
  .card--back .texture {
    background: radial-gradient(ellipse 70% 60% at 80% 20%, var(--texture) 0%, rgba(42,42,43,0) 75%);
  }

  .brand-name {
    position: absolute;
    top: 88px;
    left: 0;
    width: 100%;
    text-align: center;
    font-weight: 900;
    font-size: 42px;
    letter-spacing: 1px;
    color: var(--green);
    text-transform: uppercase;
  }

  .band {
    position: absolute;
    height: 43px;
    background: linear-gradient(90deg, rgba(79,174,58,0) 0%, rgba(47,125,42,0.75) 35%, var(--green) 100%);
  }
  .band--tagline { top: 190px; left: 20px; right: 0; }
  .band--name { top: 98px; left: 235px; right: 0; }

  .tagline {
    position: absolute;
    top: 190px;
    left: 0;
    width: 100%;
    line-height: 43px;
    text-align: center;
    font-size: 15px;
    color: var(--gold);
    padding-right: 4px;
  }

  .person {
    position: absolute;
    top: 98px;
    left: 268px;
    line-height: 43px;
    white-space: nowrap;
  }
  .person__name {
    font-weight: 700;
    font-size: 16px;
    color: var(--white);
    margin-right: 6px;
  }
  .person__role {
    font-size: 13px;
    color: var(--gold);
    letter-spacing: 0.3px;
  }

  .contacts {
    position: absolute;
    top: 180px;
    left: 241px;
    list-style: none;
  }
  .contacts li {
    display: flex;
    align-items: center;
    height: 19.5px;
    font-size: 15px;
    color: var(--gold);
  }
  .contacts svg {
    width: 12px;
    height: 12px;
    margin-right: 15px;
    fill: var(--green);
    flex: none;
  }
</style>
</head>
<body>

<section class="card card--front">
  <div class="texture" role="img" aria-label="Dark honeycomb texture"></div>
  <h1 class="brand-name">Pinevale Nutrition</h1>
  <div class="band band--tagline"></div>
  <p class="tagline">When Failure is Not and Option</p>
</section>

<section class="card card--back">
  <div class="texture" role="img" aria-label="Dark honeycomb texture"></div>
  <div class="band band--name"></div>
  <p class="person"><span class="person__name">Clive Marrowby</span><span class="person__role">DIRECTOR</span></p>
  <ul class="contacts">
    <li>
      <svg viewBox="0 0 12 12" aria-hidden="true"><path d="M2.4 0.6 L4.2 2.8 L3.3 4.1 C3.9 5.6 5.2 7 6.9 7.8 L8.1 6.9 L10.5 8.6 L9.4 10.8 C5.2 10.6 1.2 6.6 0.8 1.6 Z"/></svg>
      02 5918 2273
    </li>
    <li>
      <svg viewBox="0 0 12 12" aria-hidden="true"><path d="M0.5 2.5 H11.5 V3.3 L6 6.6 L0.5 3.3 Z M0.5 4.5 L6 7.8 L11.5 4.5 V9.5 H0.5 Z"/></svg>
      clive@pinevalenutrition.com.au
    </li>
    <li>
      <svg viewBox="0 0 12 12" aria-hidden="true"><path d="M6 0.5 A5.5 5.5 0 1 0 6 11.5 A5.5 5.5 0 1 0 6 0.5 Z M3 3 C4.5 3.5 4.5 5 3.5 5.5 C2.8 6 3.5 7.5 4.5 7.5 L4 10 C2.2 9.2 1.3 7.6 1.5 5.5 Z M7 2 C8.5 2.3 9.5 3.3 10 4.5 L8.5 5.5 L7.5 4 Z M7.5 7 L9.8 7.5 C9.3 8.8 8.3 9.8 7 10.3 Z"/></svg>
      www.pinevalenutrition.com.au
    </li>
  </ul>
</section>

</body>
</html>
```